Brightleaf Chiropractic 20th Birthday Party

We are a holistic health practice focussing on women's children's health and we need a poster and an invitation to our 20th birthday celebration.

On Sat Nov 24th 12-3pm at BCC

```html
<!DOCTYPE html>
<html lang="en">
<head>
<meta charset="utf-8">
<title>Brightleaf Chiropractic 20th Birthday Celebration</title>
<link rel="stylesheet" href="https://fonts.googleapis.com/css2?family=Oswald:wght@700&family=Arimo:wght@400;700&display=swap">
<style>
  :root {
    --page-bg: #3d464d;
    --teal: #4ec0b8;
    --brick-red: #a8200d;
    --navy: #1f5a85;
    --ring-blue: #2a3f9c;
    --white: #ffffff;
    --ribbon: #b2220f;
  }
  html, body {
    margin: 0;
    width: 1200px;
    height: 1200px;
    overflow: hidden;
    background: var(--page-bg);
  }
  .poster {
    position: absolute;
    left: 190px;
    top: 20px;
    width: 820px;
    height: 1160px;
    overflow: hidden;
  }
  .party-backdrop {
    position: absolute;
    inset: 0;
    background:
      radial-gradient(circle at 12% 35%, rgba(255, 230, 80, 0.9), transparent 30%),
      radial-gradient(circle at 15% 58%, rgba(235, 70, 120, 0.75), transparent 22%),
      radial-gradient(circle at 85% 32%, rgba(255, 140, 40, 0.85), transparent 20%),
      radial-gradient(circle at 88% 55%, rgba(200, 60, 190, 0.8), transparent 26%),
      radial-gradient(circle at 30% 78%, rgba(70, 190, 90, 0.7), transparent 20%),
      radial-gradient(circle at 70% 78%, rgba(40, 170, 230, 0.8), transparent 22%),
      radial-gradient(circle at 95% 85%, rgba(210, 130, 240, 0.8), transparent 25%),
      linear-gradient(160deg, #3fa9f0 0%, #49b8f0 40%, #2f6cf2 80%, #1f3de8 100%);
  }
  .brand-panel {
    position: absolute;
    left: 263px;
    top: 0;
    width: 290px;
    height: 295px;
    background: var(--teal);
    display: flex;
    flex-direction: column;
    align-items: center;
    justify-content: center;
    gap: 14px;
  }
  .brand-dot {
    width: 46px;
    height: 46px;
    border-radius: 50%;
    background: var(--white);
  }
  .brand-name {
    margin: 0;
    font-family: "Arimo", sans-serif;
    font-weight: 700;
    font-size: 30px;
    line-height: 1.15;
    color: var(--white);
    text-align: center;
  }
  .event-disc {
    position: absolute;
    left: 115px;
    top: 255px;
    width: 580px;
    height: 580px;
    border-radius: 50%;
    background: var(--white);
    box-shadow: 0 0 0 4px var(--white);
    border: 3px solid var(--ring-blue);
    box-sizing: border-box;
  }
  .event-text {
    position: absolute;
    left: 0;
    width: 820px;
    margin: 0;
    text-align: center;
    line-height: 1;
  }
  .headline { font-family: "Oswald", sans-serif; font-weight: 700; }
  .anniversary { top: 312px; font-size: 62px; color: var(--navy); }
  .birthday { top: 392px; font-size: 64px; color: var(--brick-red); }
  .celebration { top: 470px; font-size: 64px; color: var(--teal); }
  .detail { font-family: "Arimo", sans-serif; font-weight: 700; }
  .weekday { top: 578px; font-size: 31px; color: var(--brick-red); }
  .date { top: 612px; font-size: 78px; color: var(--navy); }
  .time { top: 696px; font-size: 35px; color: var(--teal); }
  .address-ribbon {
    position: absolute;
    left: 98px;
    top: 1037px;
    width: 620px;
    height: 60px;
  }
  .address-text {
    position: absolute;
    inset: 0;
    margin: 0;
    display: flex;
    align-items: center;
    justify-content: center;
    font-family: "Arimo", sans-serif;
    font-weight: 400;
    font-size: 46px;
    color: var(--white);
  }
</style>
</head>
<body>
  <main class="poster">
    <div class="party-backdrop" role="img" aria-label="Colourful party backdrop with balloons, bunting, streamers, confetti and fairy lights"></div>

    <header class="brand-panel">
      <span class="brand-dot"></span>
      <p class="brand-name">Brightleaf<br>Chiropractic</p>
    </header>

    <div class="event-disc"></div>

    <h1 class="event-text headline anniversary">20th</h1>
    <p class="event-text headline birthday">BIRTHDAY</p>
    <p class="event-text headline celebration">CELEBRATION</p>
    <p class="event-text detail weekday">SATURDAY, NOVEMBER</p>
    <p class="event-text detail date">24th,2018</p>
    <p class="event-text detail time">12-3pm AT BCC</p>

    <div class="address-ribbon">
      <svg width="620" height="60" viewBox="0 0 620 60" aria-hidden="true">
        <polygon points="10,0 620,0 604,30 620,60 0,60 14,30" fill="var(--ribbon)"/>
      </svg>
      <p class="address-text">14 Harbour Rd Westbrook</p>
    </div>
  </main>
</body>
</html>
```